Email Design Creative Design Needed

Our website is called CampusLedger.org. One of our competitor(varsity scout.us.com) is using the following email creative.
http://qtr.brightvelmo.com/Affiliate/Assets/3532.html
http://qtr.brightvelmo.com/Affiliate/Assets/7921.html
http://qtr.brightvelmo.com/Affiliate/Assets/8061.html

We would like to use similar email creative without copying their exact creative. You can use the above as a guide but then come up with your own version of the creative.
The above are just concepts, please be creative and come up with your own version of it, without feeling that they have been copied. Feel free to move the components around. Also, feel free to change the colours and text.

Please find attached the CampusLedger.org logo.

Reason: We would like to receive more designs.

Industry/Entity Type

College

```html
<!DOCTYPE html>
<html lang="en">
<head>
<meta charset="utf-8">
<title>CampusLedger.org — Find a Degree</title>
<link rel="stylesheet" href="https://fonts.googleapis.com/css2?family=Arimo:wght@400;700&family=Mulish:wght@800&family=Noto+Serif:wght@400&display=swap">
<style>
  :root {
    --page: #f8f8f8;
    --ink: #111111;
    --panel: #1d1d1d;
    --nav-btn: #282828;
    --yellow: #e8c93a;
    --gold: #d6a228;
    --gold-button: #d4a52a;
    --olive-gold: #a8862a;
    --link: #e0b92e;
    --white: #ffffff;
    --form-title: #35587a;
    --form-label: #2b2b2b;
    --green: #4f7a1e;
  }
  * { box-sizing: border-box; margin: 0; padding: 0; }
  html, body {
    width: 874px; height: 1200px; overflow: hidden;
    background: var(--page);
    font-family: "Arimo", Arial, sans-serif;
    color: var(--ink);
  }
  .email {
    position: absolute; left: 0; top: 0;
    width: 800px; height: 1098px;
    transform: scale(1.0925); transform-origin: 0 0;
  }
  .abs { position: absolute; }

  .preheader { left: 118px; top: 23px; font-size: 13px; }
  .preheader a, .unsubscribe a { color: var(--link); text-decoration: none; }

  .nav-band { left: 100px; top: 54px; width: 599px; height: 49px; background: var(--yellow); }
  .brand {
    left: 100px; top: 54px; width: 140px; height: 49px; background: var(--panel);
    color: var(--yellow); font-size: 22px; display: flex; align-items: center; justify-content: center;
    box-shadow: 3px 4px 5px rgba(0,0,0,.45);
  }
  .nav-item {
    top: 57px; height: 44px; background: var(--nav-btn); color: var(--white);
    font-size: 14px; display: flex; align-items: center; justify-content: center;
    box-shadow: 3px 4px 5px rgba(0,0,0,.5);
  }

  .hero-panel {
    left: 100px; top: 121px; width: 256px; height: 300px; background: var(--panel);
    border-left: 3px solid var(--gold); border-right: 3px solid var(--gold);
  }
  .hero-headline {
    left: 118px; top: 211px; color: var(--white); font-weight: 700; font-size: 17.5px; line-height: 37px;
    white-space: nowrap;
  }
  .hero-photo {
    left: 356px; top: 121px; width: 343px; height: 300px;
    background: linear-gradient(160deg, #5d6b3a 0%, #4a4a34 45%, #262622 100%);
  }
  .btn {
    display: flex; align-items: center; justify-content: center;
    font-weight: 700; color: var(--ink);
  }
  .btn-join { left: 138px; top: 350px; width: 150px; height: 39px; background: var(--gold-button); font-size: 17px; }

  .lab-photo {
    left: 102px; top: 449px; width: 278px; height: 142px;
    background: linear-gradient(100deg, #7c8a94 0%, #d8dde0 45%, #b9c4cc 70%, #6e7a82 100%);
  }
  .courses-copy { left: 408px; top: 462px; font-size: 9px; line-height: 24.5px; white-space: nowrap; }
  .courses-copy strong { display: block; }
  .courses-copy span { display: block; padding-left: 5px; }
  .btn-courses { left: 413px; top: 556px; width: 120px; height: 31px; background: var(--yellow); font-size: 13px; }

  .finder-bg {
    left: 102px; top: 591px; width: 600px; height: 348px;
    background: linear-gradient(90deg, #c6dbe6 0%, #cfc2dd 20%, #e4e0c8 38%, #f0c2cc 55%, #f3d2c6 72%, #d7e6cf 88%, #eef2ee 100%);
  }
  .finder-fade { left: 102px; top: 591px; width: 600px; height: 30px; background: rgba(245,245,245,.8); }
  .finder-band {
    left: 100px; top: 617px; width: 602px; height: 33px;
    background: linear-gradient(90deg, rgba(240,232,60,.85), rgba(246,240,80,.85));
    display: flex; align-items: center; justify-content: center;
    font-family: "Mulish", "Arimo", sans-serif; font-weight: 800; font-size: 22px; color: #262626;
  }
  .finder-copy { left: 117px; top: 666px; font-size: 9px; line-height: 24px; white-space: nowrap; }
  .career-title { left: 111px; top: 799px; font-size: 18px; font-weight: 400; white-space: nowrap; }
  .career-copy { left: 111px; top: 822px; font-size: 9px; line-height: 24.5px; white-space: nowrap; }
  .btn-more { left: 255px; top: 897px; width: 120px; height: 31px; background: var(--olive-gold); font-size: 13px; }

  .signup {
    left: 462px; top: 753px; width: 183px; height: 177px;
    background: linear-gradient(180deg, #ffffff 0%, #dfe9ee 60%, #c9d8e0 100%);
    border: 1px solid #9fb2bc; border-radius: 3px;
    box-shadow: 3px 4px 6px rgba(0,0,0,.45);
  }
  .signup-title {
    position: absolute; left: 8px; top: 3px;
    font-family: "Noto Serif", Georgia, serif; font-size: 16.5px; color: var(--form-title); white-space: nowrap;
  }
  .field-label { position: absolute; left: 14px; font-size: 6px; font-weight: 700; color: var(--form-label); }
  .field {
    position: absolute; left: 14px; width: 149px; height: 19px;
    background: #fbfbfb; border: 1px solid #9aa7ae; border-radius: 2px;
  }
  .signup-button {
    position: absolute; left: 14px; top: 133px; width: 42px; height: 19px; border-radius: 3px;
    background: linear-gradient(180deg, #7aa13a, var(--green));
    color: var(--white); font-size: 7px; font-weight: 700;
    display: flex; align-items: center; justify-content: center;
  }
  .signup-terms { position: absolute; left: 14px; top: 155px; width: 150px; font-size: 5.5px; line-height: 8px; color: #333; }
  .signup-terms em { font-style: normal; color: var(--form-title); }

  .footer-band { left: 99px; top: 965px; width: 600px; height: 59px; background: var(--gold); }
  .social {
    top: 974px; width: 42px; height: 42px; border-radius: 50%; background: var(--panel);
    display: flex; align-items: center; justify-content: center;
  }

  .unsubscribe { left: 0; top: 1042px; width: 800px; text-align: center; font-size: 14px; }
</style>
</head>
<body>
<main class="email">
  <p class="abs preheader">Can't see this Email? View it in your <a href="#">Browser</a></p>

  <div class="abs nav-band"></div>
  <div class="abs brand">your logo</div>
  <div class="abs nav-item" style="left:247px;width:129px;">Degree</div>
  <div class="abs nav-item" style="left:382px;width:135px;">Schools</div>
  <div class="abs nav-item" style="left:523px;width:135px;">Careers</div>

  <div class="abs hero-panel"></div>
  <h1 class="abs hero-headline">Start browsing today,<br>&nbsp;find a degree and discover<br>a rewarding new career!.</h1>
  <div class="abs btn btn-join">Join Us</div>
  <div class="abs hero-photo" role="img" aria-label="Graduate in cap and gown with classmates behind"></div>

  <div class="abs lab-photo" role="img" aria-label="Student in a lab coat working with glassware in a science lab"></div>
  <p class="abs courses-copy">
    <strong>Study Harbor provides courses that lead to college credit.</strong>
    <span>courses in teacher education are offered by some real schools.</span>
    <span>Learn which teacher education courses are available, what</span>
    <span>topics they cover and which ones lead to college credit.</span>
  </p>
  <div class="abs btn btn-courses">Take Courses</div>

  <div class="abs finder-bg" role="img" aria-label="Row of colourful subject textbooks labelled by school subject"></div>
  <div class="abs finder-fade"></div>
  <h2 class="abs finder-band">Quick Degree Finder</h2>
  <p class="abs finder-copy">our objective &nbsp;is to match your educational and personal goals. Whether searching for an accredited online degree by subject, level, school or<br>specific program,the CampusLedger site can help. Hundreds of degree programs from accredited online colleges and traditional schools<br>are featured on the site. Best of all, most of the degree programs found here are designed for working professionals so they can continue in<br>their current career while attending school.</p>

  <h3 class="abs career-title">Discover a rewarding new career!</h3>
  <p class="abs career-copy">Finding top universities isn't really a matter of looking at some flat, static<br>list and just reading about numbers 1, 2, 3, and 4. The top universities<br>for you are going to be different for someone else, and we can help you<br>find your own top universities</p>
  <div class="abs btn btn-more">Learn More</div>

  <form class="abs signup" aria-label="Create your account">
    <span class="signup-title">create your account</span>
    <span class="field-label" style="top:29px;">USERNAME</span>
    <span class="field" style="top:37px;"></span>
    <span class="field-label" style="top:65px;">E-MAIL ADDRESS</span>
    <span class="field" style="top:73px;"></span>
    <span class="field-label" style="top:101px;">PASSWORD</span>
    <span class="field" style="top:109px;"></span>
    <span class="signup-button">Sign Up</span>
    <span class="signup-terms">By clicking on 'Sign Up' above, you confirm that you accept the <em>Terms of Use</em>.</span>
  </form>

  <div class="abs footer-band"></div>
  <a class="abs social" style="left:307px;" href="#" aria-label="Share link">
    <svg width="20" height="20" viewBox="0 0 20 20" fill="none" stroke="#d6a228" stroke-width="2.2" stroke-linecap="round"><path d="M8.5 11.5l3-3"/><path d="M9 6.5l1.5-1.5a3 3 0 0 1 4.5 4.5L13.5 11"/><path d="M11 13.5L9.5 15a3 3 0 0 1-4.5-4.5L6.5 9"/></svg>
  </a>
  <a class="abs social" style="left:383px;" href="#" aria-label="Email a friend">
    <svg width="20" height="20" viewBox="0 0 20 20" fill="none" stroke="#d6a228" stroke-width="2" stroke-linejoin="round"><rect x="3" y="5" width="14" height="10" rx="1"/><path d="M3.5 5.5L10 11l6.5-5.5"/></svg>
  </a>
  <a class="abs social" style="left:455px;" href="#" aria-label="Visit our site">
    <svg width="20" height="20" viewBox="0 0 20 20" fill="none" stroke="#d6a228" stroke-width="2" stroke-linecap="round" stroke-linejoin="round"><path d="M4 10h11"/><path d="M11 6l4 4-4 4"/></svg>
  </a>

  <p class="abs unsubscribe">Don't want to receive email Updates? <a href="#">Unsubscribe here</a></p>
</main>
</body>
</html>
```